Business Folder

I need a fresh, modern design for a business folder. I have our company's colors, logo, and a separate file for just the graphic part of our logo as a design element. No photo, just colors, gradients, and shadows to create depth. I like the idea of a rich grey as the background, however, I realize we'd have to lighten to 'Tax Advisory Services' part of our logo.

The design would just be the 'front' or outside of the folder from Zelvora. Design file attached. You can find that here under 9 x 12 standard folder, Left and Right Pockets With Slit Both Sides:

https://www.zelvora-example.com/content.html?id=folderDownloadTemplates&rightMenuId=rightMenu&footerId=bodyFooterStyle6

```html
<!DOCTYPE html>
<html lang="en">
<head>
<meta charset="UTF-8">
<title>Kestrel Tax Advisory Services – Folder Exterior</title>
<link rel="stylesheet" href="https://fonts.googleapis.com/css2?family=Jost:wght@400;500;700&family=Montserrat:wght@800&display=swap">
<style>
  :root {
    --stage: #2b2b2b;
    --paper-light: #f1f1f2;
    --paper-mid: #dcdddf;
    --paper-dark: #c9cacc;
    --brand-navy: #1d5a86;
    --brand-blue: #0a8fd1;
    --brand-sky: #56c6e6;
    --mark-grey: #b7b8ba;
    --text-dark: #3d3f42;
    --pill-edge: #8ccbea;
  }
  * { box-sizing: border-box; margin: 0; padding: 0; }
  html, body { width: 1200px; height: 824px; overflow: hidden; background: var(--stage); }
  .folder {
    position: absolute; left: 45px; top: 42px;
    width: 1110px; height: 740px;
    display: flex;
    box-shadow: 0 18px 40px rgba(0,0,0,.45);
  }
  .panel {
    position: relative; width: 555px; height: 740px; overflow: hidden;
  }
  .panel-surface {
    position: absolute; inset: 0;
    background:
      radial-gradient(ellipse at 30% 20%, var(--paper-light) 0%, transparent 60%),
      linear-gradient(150deg, var(--paper-light) 0%, var(--paper-mid) 55%, var(--paper-dark) 100%);
  }
  .panel--back { border-right: 1px solid #cfd0d2; }
  .panel--back .panel-surface { background:
      radial-gradient(ellipse at 70% 30%, var(--paper-light) 0%, transparent 60%),
      linear-gradient(210deg, var(--paper-light) 0%, var(--paper-mid) 60%, var(--paper-dark) 100%); }

  .feature-shape { position: absolute; border-radius: 50%; }
  .panel--back .feature-shape {
    left: 137px; top: 70px; width: 280px; height: 280px;
    background: radial-gradient(circle at 40% 35%, #cfd0d2, var(--mark-grey));
  }
  .panel--front .feature-shape {
    left: 137px; top: 175px; width: 280px; height: 280px;
    background: radial-gradient(circle at 40% 35%, var(--brand-sky), var(--brand-blue) 60%, var(--brand-navy));
  }

  .brand {
    position: absolute; left: 0; right: 0; top: 58px; text-align: center;
  }
  .brand-name {
    font-family: "Montserrat", sans-serif; font-weight: 800;
    font-size: 56px; letter-spacing: 3px; color: var(--brand-navy); line-height: 1;
  }
  .brand-tagline {
    font-family: "Jost", sans-serif; font-weight: 400;
    font-size: 15px; letter-spacing: 3px; color: #6a6c70; margin-top: 6px;
  }

  .contact {
    position: absolute; left: 0; right: 0; top: 410px; text-align: center;
    font-family: "Jost", sans-serif; color: var(--text-dark);
  }
  .contact-icon {
    display: block; margin: 0 auto 6px; width: 24px; height: 24px;
  }
  .contact-line { font-size: 12px; line-height: 1.35; }
  .contact-group + .contact-group { margin-top: 14px; }
  .toll-free {
    margin-top: 12px; font-size: 20px; font-weight: 700; letter-spacing: 1px;
  }

  .web-pill {
    position: absolute; left: 50%; transform: translateX(-50%);
    width: 360px; height: 46px; border-radius: 23px;
    background: var(--brand-navy);
    border: 2px solid var(--pill-edge);
    display: flex; align-items: center; justify-content: center;
    font-family: "Jost", sans-serif; font-size: 19px; font-weight: 500;
    color: #fff; letter-spacing: .5px;
  }
  .panel--back .web-pill { top: 628px; }
  .panel--front .web-pill { top: 540px; }
</style>
</head>
<body>
  <main class="folder">
    <section class="panel panel--back" aria-label="Folder back cover">
      <div class="panel-surface"></div>
      <div class="feature-shape"></div>

      <div class="contact">
        <div class="contact-group">
          <svg class="contact-icon" viewBox="0 0 24 24" aria-hidden="true">
            <circle cx="12" cy="12" r="12" fill="var(--brand-navy)"/>
            <path d="M12 5.5a3.6 3.6 0 0 0-3.6 3.6c0 2.7 3.6 6.4 3.6 6.4s3.6-3.7 3.6-6.4A3.6 3.6 0 0 0 12 5.5z" fill="#fff"/>
            <circle cx="12" cy="9.1" r="1.3" fill="var(--brand-navy)"/>
            <rect x="8" y="17" width="8" height="1.3" rx=".6" fill="#fff"/>
          </svg>
          <p class="contact-line">1420 Harbor Lane, Ste. 210</p>
          <p class="contact-line">Fairview, IA 50000</p>
        </div>
        <div class="contact-group">
          <svg class="contact-icon" viewBox="0 0 24 24" aria-hidden="true">
            <circle cx="12" cy="12" r="12" fill="var(--brand-navy)"/>
            <rect x="6.5" y="8" width="11" height="8" rx="1" fill="none" stroke="#fff" stroke-width="1.3"/>
            <path d="M6.8 8.4 12 12.6l5.2-4.2" fill="none" stroke="#fff" stroke-width="1.3"/>
          </svg>
          <p class="contact-line">info@kestreltaxadvisory.com</p>
        </div>
        <p class="toll-free">TOLL FREE: 800-555-0142</p>
      </div>

      <div class="web-pill">www.kestreltaxadvisory.com</div>
    </section>

    <section class="panel panel--front" aria-label="Folder front cover">
      <div class="panel-surface"></div>
      <header class="brand">
        <p class="brand-name">KESTREL</p>
        <p class="brand-tagline">TAX ADVISORY SERVICES</p>
      </header>
      <div class="feature-shape"></div>
      <div class="web-pill">www.kestreltaxadvisory.com</div>
    </section>
  </main>
</body>
</html>
```